Spray Foam Company Business Card

We need a business card designed for our spray foam insulation and roof coatings business. We handle residential and commercial projects.
Construction
We would like it to say:
R & K Spray
with these bullet points
-foam insulation
-waterproofing roof system
-water proofing foundation systems
website is rksprayfoaminsulation.example (this was just purchased)
office phone : 630-482-9164
And 3 cards with names on them the names are :
Derek Halvorsen
Curtis Pennington
Rob Stallworth
maybe the bullet points can go on the back?
if you go this website it is another division of our company and you can see the font we use in the R & K. We do not want to use the same half circles that it has just the lettering
www.coatedrightforyears.example

```html
<!DOCTYPE html>
<html lang="en">
<head>
<meta charset="utf-8">
<title>R &amp; K Spray – Business Cards</title>
<link rel="stylesheet" href="https://fonts.googleapis.com/css2?family=Exo+2:wght@400;600&family=Kalam:wght@400&display=swap">
<style>
  :root {
    --backdrop: #ece8e2;
    --ink-black: #0b0b0b;
    --paper-white: #ffffff;
    --brand-blue: #2f3f9f;
    --brand-purple: #5b2266;
    --brand-red: #cc2a2c;
    --brand-orange: #e2502a;
    --brand-yellow: #e2b52c;
    --divider-grey: #8a8a8a;
    --text-dark: #161616;
    --brand-spectrum: linear-gradient(90deg, var(--brand-blue) 0%, var(--brand-purple) 35%, var(--brand-red) 65%, var(--brand-orange) 85%, var(--brand-yellow) 100%);
  }
  * { box-sizing: border-box; margin: 0; padding: 0; }
  html, body {
    width: 1200px;
    height: 2239px;
    overflow: hidden;
    background: var(--backdrop);
    font-family: "Exo 2", sans-serif;
  }
  .card-sheet { position: relative; width: 1200px; height: 2239px; }
  .card {
    position: absolute;
    left: 160px;
    width: 880px;
    height: 503px;
    overflow: hidden;
    box-shadow: 0 6px 18px rgba(0,0,0,0.18);
  }
  .card--back-spectrum { top: 45px;
    background: linear-gradient(155deg, var(--brand-blue) 0%, var(--brand-purple) 28%, var(--brand-red) 55%, var(--brand-orange) 78%, var(--brand-yellow) 100%);
    color: var(--paper-white); }
  .card--front-dark { top: 593px; background: var(--ink-black); color: var(--paper-white); }
  .card--back-dark { top: 1141px; background: var(--ink-black); color: var(--paper-white); }
  .card--front-light { top: 1689px; background: var(--paper-white); color: var(--text-dark); }

  .rule { position: absolute; height: 4px; }
  .rule--white { background: var(--paper-white); height: 3px; }
  .rule--spectrum { background: var(--brand-spectrum); }

  .back .rule--upper { top: 95px; left: 150px; width: 650px; }
  .back .rule--lower { top: 320px; left: 110px; width: 720px; }
  .front .rule--upper { top: 60px; left: 0; width: 720px; }
  .front .rule--lower { top: 275px; left: 100px; width: 780px; }

  .wordmark {
    position: absolute;
    left: 0; right: 0;
    text-align: center;
    font-family: "Exo 2", sans-serif;
    font-weight: 600;
    font-size: 104px;
    line-height: 1;
    letter-spacing: 1px;
  }
  .back .wordmark { top: 155px; color: var(--paper-white); }
  .front .wordmark { top: 112px; color: var(--brand-red); }

  .service-list {
    position: absolute;
    right: 60px;
    top: 345px;
    list-style: none;
    text-align: right;
    font-size: 27px;
    font-weight: 600;
    line-height: 1.3;
  }

  .holder-name {
    position: absolute;
    left: 95px;
    top: 350px;
    font-family: "Kalam", cursive;
    font-size: 38px;
  }
  .contact-divider {
    position: absolute;
    left: 410px;
    top: 330px;
    width: 1px;
    height: 115px;
    background: var(--divider-grey);
  }
  .contact-block {
    position: absolute;
    left: 435px;
    top: 345px;
    font-size: 26px;
    line-height: 1.45;
  }
</style>
</head>
<body>
<main class="card-sheet">

  <section class="card card--back-spectrum back" aria-label="Card back, colour version">
    <div class="rule rule--white rule--upper"></div>
    <div class="wordmark">R &amp; K Spray</div>
    <div class="rule rule--white rule--lower"></div>
    <ul class="service-list">
      <li>Foam Insulation</li>
      <li>Waterproofing Roof Systems</li>
      <li>Waterproofing Foundation Systems</li>
    </ul>
  </section>

  <section class="card card--front-dark front" aria-label="Card front, dark version">
    <div class="rule rule--spectrum rule--upper"></div>
    <div class="wordmark">R &amp; K Spray</div>
    <div class="rule rule--spectrum rule--lower"></div>
    <p class="holder-name">Derek Halvorsen</p>
    <div class="contact-divider"></div>
    <div class="contact-block">
      <p>rksprayfoaminsulation.example</p>
      <p>630-482-9164</p>
    </div>
  </section>

  <section class="card card--back-dark back" aria-label="Card back, dark version">
    <div class="rule rule--spectrum rule--upper"></div>
    <div class="wordmark">R &amp; K Spray</div>
    <div class="rule rule--spectrum rule--lower"></div>
    <ul class="service-list">
      <li>Foam Insulation</li>
      <li>Waterproofing Roof Systems</li>
      <li>Waterproofing Foundation Systems</li>
    </ul>
  </section>

  <section class="card card--front-light front" aria-label="Card front, light version">
    <div class="rule rule--spectrum rule--upper"></div>
    <div class="wordmark">R &amp; K Spray</div>
    <div class="rule rule--spectrum rule--lower"></div>
    <p class="holder-name">Derek Halvorsen</p>
    <div class="contact-divider"></div>
    <div class="contact-block">
      <p>rksprayfoaminsulation.example</p>
      <p>630-482-9164</p>
    </div>
  </section>

</main>
</body>
</html>
```